Wedding Startup Full Website Design

We've just completed our online platform and need to create a website that represents our brand and vision, and clearly communicates our features and value proposition to potential users. There are a minimum of 4 pages that need to be designed. One geared toward wedding professionals (venues/vendors/coordinators), another toward engaged couples, one showcasing features, and an 'About Us' page.

The designer will creative freedom to create a unique UI/UX as long as it represents our brand and is relevant to our target audience/market. The ideal candidate will be able to assume the mindset of someone working in the wedding industry and/or an engaged couple. Ability to create illustrations is a plus.

Copy will be provided as needed. We will reimburse for stock images (pending approval before purchasing), but sourcing the stock images will be the responsibility of the designer.

Our current website: https://www.marquiso.com
Updates

Still waiting for a design that stands out from the rest and aligns with the creative brief.

Target Market(s)

Wedding Professionals and Engaged Couples

Industry/Entity Type

Wedding

Number of Pages Required

4 page

Font styles to use
Sans Serif

Colors
ffffff
fbd4d5
f59195
33a6d7
cadf82
86cfc6

Requirements
Must have
• Common sense stuff like having a unified brand that accurately represents our platform, speaks to our target market, and clearly articulates our vision
Nice to have
• Illustrations
Should not have
• Overly cheesy or childish. We want to be professional but still embrace the wedding culture.

```html
<!DOCTYPE html>
<html lang="en">
<head>
<meta charset="utf-8">
<title>Marquiso — Simpler Event Planning</title>
<link href="https://fonts.googleapis.com/css2?family=Montserrat:wght@300;400;500;600;700&display=swap" rel="stylesheet">
<style>
:root{
  --white:#ffffff;
  --blush:#fbd4d5;
  --coral:#f59195;
  --sky:#33a6d7;
  --lime:#cadf82;
  --teal:#86cfc6;
  --ink:#2b2b2b;
  --muted:#555;
  --night:#141517;
  --night-2:#1e2024;
}
*{box-sizing:border-box;margin:0;padding:0}
html,body{width:1200px;height:3523px;overflow:hidden}
body{font-family:"Montserrat",sans-serif;color:var(--ink);background:var(--white);position:relative}
/* header */
.site-header{position:absolute;left:0;top:0;width:1200px;height:106px;background:rgba(20,16,30,.85);z-index:2}
.brand{position:absolute;left:84px;top:26px;display:flex;align-items:center;gap:12px;color:var(--white);font-weight:600;font-size:40px;letter-spacing:-.5px}
.brand-square{width:22px;height:22px;border:3px solid var(--white)}
.main-nav{position:absolute;right:86px;top:40px;display:flex;gap:36px}
.main-nav a{color:var(--white);text-decoration:none;font-size:15px;font-weight:500}
/* hero */
.hero{position:absolute;left:0;top:0;width:1200px;height:618px;background:
 radial-gradient(ellipse at 60% 55%,#c9a6f2 0%,#8a4fd6 30%,#5b2aa6 60%,#2c1458 100%)}
.hero-box{position:absolute;left:89px;top:247px;width:477px;height:234px;border:3px solid var(--white);background:rgba(30,20,50,.45);text-align:center;color:var(--white);padding-top:46px}
.hero-box h1{font-size:33px;font-weight:500;letter-spacing:.5px;white-space:nowrap}
.hero-box p{font-size:21px;font-weight:600;letter-spacing:1px;margin-top:4px;white-space:nowrap}
.btn-coral{display:inline-block;margin-top:24px;background:var(--coral);color:var(--white);font-size:14px;font-weight:500;padding:10px 26px;border-radius:3px}
/* intro */
.intro{position:absolute;left:0;top:618px;width:1200px;height:509px;background:var(--blush);text-align:center}
.intro .kicker{position:absolute;top:82px;width:100%;font-size:16px;font-weight:600}
.intro h2{position:absolute;top:96px;width:100%;font-size:94px;line-height:110px;font-weight:500;letter-spacing:-1px}
.intro .copy{position:absolute;left:228px;top:222px;width:744px;font-size:13.5px;line-height:22px;color:#444}
.intro .copy p+p{margin-top:20px}
.btn-sky{position:absolute;left:505px;top:370px;width:188px;height:52px;background:var(--sky);color:var(--white);font-size:18px;line-height:52px;border-radius:2px}
/* steps */
.steps-title{position:absolute;top:1196px;width:1200px;text-align:center;font-size:54px;font-weight:400;color:#444}
.step-line{position:absolute;top:1339px;height:3px}
.step{position:absolute;top:1313px;width:330px}
.step-num{position:absolute;left:0;top:0;width:52px;height:52px;border-radius:50%;color:var(--white);font-size:22px;text-align:center;line-height:52px;box-shadow:0 0 0 5px rgba(255,255,255,.9),0 2px 6px rgba(0,0,0,.2)}
.step h3{position:absolute;left:70px;top:0;font-size:19px;font-weight:500}
.step p{position:absolute;left:70px;top:34px;width:220px;font-size:12.5px;line-height:20px;color:#555}
.device-wall{position:absolute;left:160px;top:1456px;width:880px;height:420px}
/* features band */
.features{position:absolute;left:0;top:1960px;width:1200px;height:388px;background:var(--sky);color:var(--white)}
.feature{position:absolute;top:78px;width:340px;text-align:center}
.feature-icon{width:122px;height:122px;border-radius:50%;background:var(--white);margin:0 auto;position:relative}
.feature h3{font-size:18px;font-weight:500;margin-top:24px}
.feature p{font-size:12.5px;line-height:18px;margin:6px auto 0;width:300px}
/* why */
.why{position:absolute;left:0;top:2348px;width:1200px;height:639px;overflow:hidden}
.why h2{position:absolute;top:88px;width:100%;text-align:center;color:var(--sky);font-size:38px;font-weight:400}
.reason{position:absolute;width:290px}
.reason h3{font-size:16px;font-weight:500;margin-bottom:8px}
.reason p{font-size:11.5px;line-height:18px;color:#555}
.reason.right{text-align:right}
.reason.center{text-align:center}
.hub{position:absolute;left:413px;top:352px;width:376px;height:376px;border-radius:50%;background:var(--teal);box-shadow:0 0 0 8px #e9f6f4}
.hub-core{position:absolute;left:26px;top:26px;width:324px;height:324px;border-radius:50%;background:var(--sky);color:var(--white);font-size:56px;font-weight:500;text-align:center;padding-top:88px}
.orbit{position:absolute;width:94px;height:94px;border-radius:50%;background:var(--white);box-shadow:0 0 0 6px #dfeeee,0 2px 6px rgba(0,0,0,.12)}
.orbit span{position:absolute;left:22px;top:22px;width:50px;height:50px;border-radius:50%}
/* cta */
.cta{position:absolute;left:0;top:2987px;width:1200px;height:237px;background:var(--coral);color:var(--white)}
.cta h2{position:absolute;left:155px;top:60px;font-size:36px;font-weight:400}
.cta p{position:absolute;left:155px;top:110px;width:560px;font-size:13px;line-height:21px}
.cta .btn{position:absolute;left:735px;top:84px;width:310px;height:75px;background:var(--sky);border:3px solid rgba(255,255,255,.35);box-shadow:0 4px 8px rgba(0,0,0,.25);font-size:26px;text-align:center;line-height:69px}
/* footer */
.site-footer{position:absolute;left:0;top:3224px;width:1200px;height:299px;background:linear-gradient(160deg,var(--night-2),var(--night));color:var(--white)}
.footer-nav{position:absolute;top:46px;width:100%;text-align:center;font-size:14px;font-weight:500;letter-spacing:.5px}
.footer-nav span{margin:0 14px}
.email{position:absolute;left:303px;top:91px;width:413px;height:50px;background:var(--white);color:#999;font-size:13px;font-style:italic;padding:17px 14px}
.subscribe{position:absolute;left:735px;top:91px;width:162px;height:50px;background:var(--sky);font-size:17px;font-weight:600;text-align:center;line-height:50px}
.socials{position:absolute;left:507px;top:171px;display:flex;gap:9px}
.socials span{width:37px;height:37px;border-radius:50%;background:#d9d9d9}
.copyright{position:absolute;top:230px;width:100%;text-align:center;font-size:13px}
</style>
</head>
<body>

<section class="hero" role="img" aria-label="Wedding reception hall lit in purple with decorated round tables"></section>

<header class="site-header">
  <div class="brand"><span class="brand-square"></span>Marquiso</div>
  <nav class="main-nav">
    <a href="#">Home</a><a href="#">About us</a><a href="#">Wedding Professionals</a><a href="#">Features</a><a href="#">Contact us</a>
  </nav>
</header>

<div class="hero-box">
  <h1>WELCOME TO MARQUISO</h1>
  <p>SIMPLER EVENT PLANNING</p>
  <span class="btn-coral">GET STARTED</span>
</div>

<section class="intro">
  <div class="kicker">Welcome to</div>
  <h2>Marquiso</h2>
  <div class="copy">
    <p>Weddings are one the most memorable events in people's life. Unfortunately planning a wedding is filled with stress, often leaving wedding professionals and their clients with soured memories.</p>
    <p>Our vision at Marquiso is to revamp the way weddings are planned on both sides of the process (wedding professionals and their clients). We aim to reduce the stress of everyone involved, and make the engagement season and wedding day memorable for the right reasons.</p>
  </div>
  <div class="btn-sky">About Marquiso</div>
</section>

<h2 class="steps-title">How To Get Started</h2>
<div class="step-line" style="left:140px;width:340px;background:linear-gradient(90deg,var(--sky),var(--coral))"></div>
<div class="step-line" style="left:500px;width:340px;background:var(--coral)"></div>
<div class="step" style="left:90px">
  <div class="step-num" style="background:var(--sky)">01</div>
  <h3>Sign Up</h3>
  <p>Create a free account on Marquiso to access popular collaboration tools.</p>
</div>
<div class="step" style="left:452px">
  <div class="step-num" style="background:var(--coral)">02</div>
  <h3>Collaborate</h3>
  <p>Add clients within the application to better organize and manage event details.</p>
</div>
<div class="step" style="left:813px">
  <div class="step-num" style="background:var(--coral)">03</div>
  <h3>Connect</h3>
  <p>Linking your bank account within Marquiso to allow for seamless payments and monitoring.</p>
</div>

<svg class="device-wall" viewBox="0 0 880 420" role="img" aria-label="Tablet screens showing the planning dashboard">
  <rect x="2" y="62" width="250" height="290" rx="14" fill="#f4f4f4" stroke="#e2e2e2"/>
  <rect x="628" y="62" width="250" height="290" rx="14" fill="#f4f4f4" stroke="#e2e2e2"/>
  <rect x="40" y="92" width="190" height="230" fill="#e9ecef"/>
  <rect x="650" y="92" width="190" height="230" fill="#e9ecef"/>
  <rect x="182" y="14" width="516" height="396" rx="22" fill="#fafafa" stroke="#d8d8d8" stroke-width="2"/>
  <rect x="224" y="50" width="430" height="310" fill="#ffffff" stroke="#555"/>
  <rect x="224" y="50" width="430" height="12" fill="#e4e6ea"/>
  <rect x="224" y="62" width="62" height="298" fill="#f0f1f3"/>
  <rect x="286" y="62" width="368" height="26" fill="#dfe9f5"/>
  <g fill="#cfd3d8">
    <rect x="300" y="108" width="240" height="6"/><rect x="300" y="124" width="300" height="6"/>
    <rect x="300" y="150" width="200" height="6"/><rect x="300" y="176" width="260" height="6"/>
    <rect x="300" y="202" width="220" height="6"/><rect x="300" y="228" width="300" height="6"/>
    <rect x="300" y="254" width="180" height="6"/><rect x="300" y="280" width="280" height="6"/>
  </g>
</svg>

<section class="features">
  <div class="feature" style="left:79px">
    <div class="feature-icon" role="img" aria-label="Envelope icon"><svg width="122" height="122" viewBox="0 0 122 122"><rect x="34" y="44" width="54" height="38" fill="#e94c4c"/><path d="M34 44 L61 66 L88 44" fill="none" stroke="#fff" stroke-width="3"/></svg></div>
    <h3>Realtime Collaboration</h3>
    <p>There are often disconnects in the communication channel. At the core of Marquiso we ensure everyone is updated in real time with event information.</p>
  </div>
  <div class="feature" style="left:430px">
    <div class="feature-icon" role="img" aria-label="Cloud upload icon"><svg width="122" height="122" viewBox="0 0 122 122"><path d="M38 70 a14 14 0 0 1 6-27 a18 18 0 0 1 34 2 a12 12 0 0 1 6 25 Z" fill="none" stroke="#333" stroke-width="3"/><path d="M61 88 V58 M52 66 L61 57 L70 66" fill="none" stroke="#33a6d7" stroke-width="4"/></svg></div>
    <h3>Cloud Storage</h3>
    <p>No longer do you have to remember where every piece of information is saved. With Marquiso all your information is available in one central location.</p>
  </div>
  <div class="feature" style="left:794px">
    <div class="feature-icon" role="img" aria-label="Bell icon"><svg width="122" height="122" viewBox="0 0 122 122"><path d="M46 78 V58 a15 15 0 0 1 30 0 V78 Z" fill="#f5b622"/><rect x="42" y="78" width="38" height="5" fill="#e89a10"/><circle cx="78" cy="80" r="10" fill="#e94c4c"/></svg></div>
    <h3>Notifications &amp; Deadlines</h3>
    <p>Every detail is important and matters. Marquiso helps make sure that all the information for an event are inputted and updated in a timely manner.</p>
  </div>
</section>

<section class="why">
  <h2>WHY MARQUISO</h2>
  <div class="reason center" style="left:455px;top:176px">
    <h3>Accessible on Any Device</h3>
    <p>Flexibility is key, which is why Marquiso's platform was built to be accessed on your phone, tablet or desktop.</p>
  </div>
  <div class="reason right" style="left:90px;top:346px">
    <h3>Better Client Reviews</h3>
    <p>With Marquiso you can offer your clients an experience they will rave about, leading to better reviews and more clients.</p>
  </div>
  <div class="reason" style="left:829px;top:346px">
    <h3>Simplified Organization</h3>
    <p>Marquiso was built with organization in mind. All event details are in one place making executing an event easier.</p>
  </div>
  <div class="reason right" style="left:34px;top:478px">
    <h3>Saves Everyone Time</h3>
    <p>Marquiso streamlines certain processes allowing you to spend more time on the things your want to or just relax!</p>
  </div>
  <div class="reason" style="left:883px;top:478px">
    <h3>Lower Transaction Fees</h3>
    <p>We offer the lowest online processing fees (2.65%) in the wedding industry, meaning you keep more of your money.</p>
  </div>
  <div class="hub"><div class="hub-core">Marquiso</div></div>
  <div class="orbit" style="left:556px;top:272px" role="img" aria-label="Devices illustration"><span style="background:#f59195"></span></div>
  <div class="orbit" style="left:392px;top:347px" role="img" aria-label="Speech bubbles illustration"><span style="background:#86cfc6"></span></div>
  <div class="orbit" style="left:709px;top:347px" role="img" aria-label="Clipboard illustration"><span style="background:#f5d8b0"></span></div>
  <div class="orbit" style="left:333px;top:516px" role="img" aria-label="Clock illustration"><span style="background:#e94c4c"></span></div>
  <div class="orbit" style="left:763px;top:484px" role="img" aria-label="Payment card illustration"><span style="background:#f5b622"></span></div>
</section>

<section class="cta">
  <h2>Get Started Today</h2>
  <p>We recently launched a demo version of Marquiso to allow users to see and interact with our platform. Create a free account and see how Marquiso is changing the wedding planning process!</p>
  <div class="btn">Access Demo</div>
</section>

<footer class="site-footer">
  <div class="footer-nav"><span>HOME</span>|<span>ABOUT US</span>|<span>WEDDING PROFESSIONALS</span>|<span>FEATURES</span>|<span>CONTACT US</span></div>
  <div class="email">Enter your email...</div>
  <div class="subscribe">SUBSCRIBE</div>
  <div class="socials" aria-label="Social links"><span></span><span></span><span></span><span></span><span></span></div>
  <div class="copyright">Copyright © 2018 Marquiso. All rights reserved.</div>
</footer>

</body>
</html>
```